label design for coffee bean packaging

Logo will be provided. Label design for package of coffee beans for a micro roasted coffee company. Need to have space to write in origin, weight with check box for 1/4, 1/2, 1lb. Need to have check boxes for Light, Medium, Dark. Creative unique label design with boarders and fun, modern design. Company name is Cedar Brook Roasting Company. See attached logo. I have source files for logo if needed for design.
Industry/Entity Type
Coffee Shop
Font styles to use
Other font styles liked:
- Montez, kautiva cyrillic, uniform bold
Colors
f78f20
faa54b
f37122
fece3e
acd036
Requirements
Must have
- logo included in the design

```html
<!DOCTYPE html>
<html lang="en">
<head>
<meta charset="utf-8">
<title>Cedar Brook Roasting Company – Coffee Bean Box</title>
<link href="https://fonts.googleapis.com/css2?family=Montserrat:ital,wght@0,600;0,700;1,800&display=swap" rel="stylesheet">
<style>
  :root {
    --bg-top: #483b60;
    --bg-bottom: #574878;
    --kraft: #c9a168;
    --kraft-side: #bb9259;
    --kraft-edge: #a98149;
    --ink: #2b2118;
    --brand-brown: #5a3826;
    --bean-dark: #3a2416;
    --bean-mid: #6b4128;
  }
  * { margin: 0; padding: 0; box-sizing: border-box; }
  html, body { width: 1200px; height: 840px; overflow: hidden; }
  body {
    background: linear-gradient(180deg, var(--bg-top), var(--bg-bottom));
    font-family: "Montserrat", Arial, sans-serif;
    position: relative;
  }
  .package {
    position: absolute;
    left: 452px;
    top: 140px;
    width: 296px;
    height: 620px;
    display: flex;
  }
  .side-panel {
    width: 48px;
    height: 100%;
    background: var(--kraft-side);
    border-right: 2px dashed var(--kraft-edge);
    position: relative;
  }
  .side-name {
    position: absolute;
    left: 50%;
    top: 420px;
    transform: translate(-50%, -50%) rotate(-90deg);
    white-space: nowrap;
    font-size: 16px;
    font-weight: 800;
    font-style: italic;
    color: #111;
  }
  .front-panel {
    position: relative;
    flex: 1;
    background: var(--kraft);
  }
  .brand-name {
    position: absolute;
    left: 24px;
    top: 200px;
    width: 200px;
    height: 120px;
    display: flex;
    align-items: center;
    justify-content: center;
    text-align: center;
    font-size: 24px;
    font-weight: 700;
    line-height: 1.2;
    color: var(--brand-brown);
  }
  .roast-options {
    position: absolute;
    left: 0;
    top: 374px;
    width: 100%;
    display: flex;
    justify-content: center;
    gap: 12px;
  }
  .option {
    display: flex;
    align-items: center;
    gap: 4px;
    font-size: 13px;
    font-weight: 700;
    color: var(--ink);
    white-space: nowrap;
  }
  .check-box {
    width: 12px;
    height: 12px;
    border: 1.5px solid var(--ink);
    display: block;
  }
  .bean-window {
    position: absolute;
    left: 40px;
    top: 402px;
    width: 168px;
    height: 100px;
    border-radius: 10px;
    background: radial-gradient(circle at 40% 40%, var(--bean-mid), var(--bean-dark));
  }
  .origin-line {
    position: absolute;
    left: 30px;
    top: 516px;
    width: 188px;
    display: flex;
    align-items: flex-end;
    gap: 6px;
    font-size: 11px;
    font-weight: 700;
    color: var(--ink);
  }
  .write-in {
    flex: 1;
    border-bottom: 1.5px solid var(--ink);
    height: 12px;
  }
  .weight-options {
    position: absolute;
    left: 0;
    top: 542px;
    width: 100%;
    display: flex;
    justify-content: center;
    gap: 8px;
  }
  .weight-options .option { font-size: 11px; }
  .weight-options .check-box { width: 10px; height: 10px; }
  .website {
    position: absolute;
    left: 0;
    bottom: 24px;
    width: 100%;
    text-align: center;
    font-size: 11px;
    font-weight: 700;
    color: var(--ink);
  }
</style>
</head>
<body>
  <div class="package">
    <div class="side-panel">
      <span class="side-name">Cedar Brook Roasting Company</span>
    </div>
    <div class="front-panel">
      <div class="brand-name">Cedar Brook Roasting Company</div>

      <div class="roast-options">
        <span class="option">
          <svg class="check-box" viewBox="0 0 12 12" aria-hidden="true"><path d="M2 6.5 L5 9 L10 2.5" fill="none" stroke="#2b2118" stroke-width="2"/></svg>Light
        </span>
        <span class="option"><span class="check-box"></span>Medium</span>
        <span class="option"><span class="check-box"></span>Dark</span>
      </div>

      <div class="bean-window" role="img" aria-label="Window showing roasted coffee beans"></div>

      <div class="origin-line">Origin:<span class="write-in"></span></div>

      <div class="weight-options">
        <span class="option">Weight:</span>
        <span class="option"><span class="check-box"></span>1/4 lb</span>
        <span class="option"><span class="check-box"></span>1/2 lb</span>
        <span class="option"><span class="check-box"></span>1 lb</span>
      </div>

      <div class="website">cedarbrookroastingcompany.com</div>
    </div>
  </div>
</body>
</html>
```